Coastal Gin Label Design

We are needing a nautical/coastal themed label for our upcoming gin release.

We have saltbush, cucumber, juniper, and quandong being used in this gin.

Name of the Gin; Harbor Nights

The logo attached is the company logo, but doesn't have to be used on the front of the label, ie it can just be the name Fernholdes somewhere on the front.
Bottle specs attached as well so you can accurately represent the bottle- this bottle is also clear.

Target Market(s)

Women 25- 45

Font styles to use
Serif
Decorative

Colors
d5edf4
86cae7
33a6d7
86cfc6
cfeae6
ffffff
f6faec
ecf7fb
fefeff

Requirements
Must have
• Ocean/Coastal vibe to the label
Nice to have
• Blues,Whites clean and crisp
Should not have
• No generic word art look to it.
A dark mood

```html
<!DOCTYPE html>
<html lang="en">
<head>
<meta charset="utf-8">
<title>Harbor Nights Gin Label</title>
<link rel="stylesheet" href="https://fonts.googleapis.com/css2?family=Roboto+Slab:wght@400;700&family=Libre+Baskerville&display=swap">
<style>
  :root {
    --page: #dfe5ec;
    --paper: #fefeff;
    --edge: #9fcfd6;
    --frame: #8fbcc4;
    --title: #2a8fc6;
    --sea-foam: #d9e6e2;
    --sea-light: #7faeb1;
    --sea-mid: #4d7e86;
    --sea-deep: #35616b;
    --sand-light: #d6c9b2;
    --sand: #b9a78d;
    --ink: #2d2d2d;
    --gin-text: #e4e7e6;
  }
  * { box-sizing: border-box; margin: 0; padding: 0; }
  html, body { width: 794px; height: 1200px; overflow: hidden; }
  body { background: var(--page); position: relative; }

  .label {
    position: absolute;
    left: 37px; top: 246px;
    width: 720px; height: 707px;
    background: var(--paper);
    overflow: hidden;
  }
  .edge { position: absolute; z-index: 5; }
  .edge-top, .edge-bottom { left: 0; right: 0; height: 7px; }
  .edge-left, .edge-right { top: 0; bottom: 0; width: 7px; }
  .edge-top {
    top: 0;
    background:
      linear-gradient(315deg, transparent 50%, var(--edge) 50%) 0 0/10px 7px repeat-x,
      linear-gradient(45deg, transparent 50%, var(--edge) 50%) 0 0/10px 7px repeat-x;
  }
  .edge-bottom {
    bottom: 0;
    background:
      linear-gradient(135deg, transparent 50%, var(--edge) 50%) 0 0/10px 7px repeat-x,
      linear-gradient(225deg, transparent 50%, var(--edge) 50%) 0 0/10px 7px repeat-x;
  }
  .edge-left {
    left: 0;
    background:
      linear-gradient(315deg, transparent 50%, var(--edge) 50%) 0 0/7px 10px repeat-y,
      linear-gradient(225deg, transparent 50%, var(--edge) 50%) 0 0/7px 10px repeat-y;
  }
  .edge-right {
    right: 0;
    background:
      linear-gradient(45deg, transparent 50%, var(--edge) 50%) 0 0/7px 10px repeat-y,
      linear-gradient(135deg, transparent 50%, var(--edge) 50%) 0 0/7px 10px repeat-y;
  }

  .frame {
    position: absolute;
    left: 34px; right: 34px; top: 32px; height: 330px;
    border: 2px solid var(--frame);
  }
  .frame-inner {
    position: absolute;
    left: 44px; right: 44px; top: 42px; height: 320px;
    border: 1px solid var(--frame);
  }

  .maker {
    position: absolute;
    top: 92px; left: 0; right: 0;
    text-align: center;
    font-family: "Libre Baskerville", serif;
    font-size: 20px;
    letter-spacing: 1px;
    color: var(--ink);
  }

  .product-name {
    position: absolute;
    top: 160px; left: 0; right: 0;
    text-align: center;
    font-family: "Roboto Slab", serif;
    font-weight: 700;
    font-size: 80px;
    line-height: 84px;
    letter-spacing: 2px;
    color: var(--title);
  }

  .sea-art {
    position: absolute;
    left: 0; right: 0; top: 336px; bottom: 0;
    background: linear-gradient(180deg,
      var(--sea-foam) 0%,
      var(--sea-light) 10%,
      var(--sea-mid) 28%,
      var(--sea-deep) 42%,
      var(--sea-light) 55%,
      var(--sand-light) 68%,
      var(--sand) 84%,
      var(--sand-light) 100%);
  }

  .spec-box {
    position: absolute;
    left: 206px; top: 535px;
    width: 300px; height: 134px;
    border: 2px solid var(--paper);
    border-radius: 6px;
  }
  .spec-pill {
    position: absolute;
    left: 50%; transform: translateX(-50%);
    background: var(--paper);
    border-radius: 8px;
    padding: 1px 10px;
    font-family: "Roboto Slab", serif;
    font-weight: 700;
    font-size: 13px;
    color: var(--ink);
    white-space: nowrap;
  }
  .spec-abv { top: -11px; }
  .spec-volume { bottom: -11px; }
  .spec-type {
    position: absolute;
    left: 0; right: 0; top: 36px;
    text-align: center;
    font-family: "Roboto Slab", serif;
    font-weight: 700;
    font-size: 50px;
    line-height: 56px;
    color: var(--gin-text);
  }

  .base-rule {
    position: absolute;
    left: 38px; width: 632px; top: 686px;
    height: 3px;
    background: var(--paper);
  }
</style>
</head>
<body>
  <section class="label">
    <div class="frame"></div>
    <div class="frame-inner"></div>

    <p class="maker">FERNHOLDES</p>
    <h1 class="product-name">HARBOR<br>NIGHTS</h1>

    <div class="sea-art" role="img" aria-label="Watercolour sea with rolling teal waves over a sandy shore"></div>

    <div class="spec-box">
      <span class="spec-pill spec-abv">40% alc/vol</span>
      <p class="spec-type">GIN</p>
      <span class="spec-pill spec-volume">700 ml</span>
    </div>

    <div class="base-rule"></div>

    <div class="edge edge-top"></div>
    <div class="edge edge-bottom"></div>
    <div class="edge edge-left"></div>
    <div class="edge edge-right"></div>
  </section>
</body>
</html>
```